A5 Certificate for a running Brisora Challenge

I would like a certificate designed called the "Brisora 50K Running Challenge"

It is presented to people that have run 50k in Mallorca across 10 runs. So they have to run 10 runs with a minimum distance of 5K per run. This gives a total of 50k.

The certificate will need:

1. Map of Mallorca in the background
2. Picture of a runner
3. Main title at the front to say "Brisora 50k Running Challenge"
4. Space to put the runners name on it. "Awarded to:"
5. Space to put the date the certificate is awarded. "Date Awarded:"

The design is then up to you but it needs to look official and professional. It is designed for teenagers so it needs to be "cool" and bold.

Any questions please ask.

Target Market(s)

Teenagers who want something cool and bold.

Font styles to use
Sans Serif

Colors
0556a4
fbee3f
33a6d7

Requirements
Must have
• 1. Map of Mallorca in the background
• 2. Picture of a runner
• 3. Main title at the front to say "Brisora 50k Running Challenge"
• 4. Space to put the runners name on it. "Awarded to:"
• 5. Space to put the date the certificate is awarded. "Date Awarded:"
Nice to have
• Mallorca is a sunny holiday location so it would be good to have sea blue colours and the sun in the design. to show the running challenge was done on a holiday island.

```html
<!DOCTYPE html>
<html lang="en">
<head>
<meta charset="utf-8">
<title>Brisora 50K Running Challenge Certificate</title>
<link href="https://fonts.googleapis.com/css2?family=Montserrat:wght@700;800&family=Great+Vibes&family=Tinos&display=swap" rel="stylesheet">
<style>
  :root {
    --navy: #1b3a5a;
    --ink: #24405e;
    --sea-deep: #0556a4;
    --sea: #1f8fd6;
    --sky: #33a6d7;
    --mist: #bfe0f5;
    --island: #cfe6f7;
    --island-edge: #a9d0ee;
    --runner: #29a6e0;
    --rule: #8a95a3;
    --paper: #ffffff;
  }
  * { margin: 0; padding: 0; box-sizing: border-box; }
  html, body { width: 1200px; height: 848px; overflow: hidden; background: var(--paper); }
  .certificate { position: relative; width: 1200px; height: 848px; overflow: hidden; background: var(--paper); }
  .waves { position: absolute; inset: 0; width: 1200px; height: 848px; }
  .island-map {
    position: absolute; left: 465px; top: 92px; width: 700px; height: 552px;
    border-radius: 46% 38% 44% 52% / 40% 48% 46% 54%;
    background: radial-gradient(ellipse at 40% 45%, #e4f1fb 0%, var(--island) 55%, var(--island-edge) 100%);
  }
  .runner-figure {
    position: absolute; left: 900px; top: 240px; width: 255px; height: 335px;
    border-radius: 48% 48% 30% 30% / 30% 30% 20% 20%;
    background: var(--runner);
  }
  .heading-script {
    position: absolute; left: 0; width: 990px; top: 78px; text-align: center;
    font-family: "Great Vibes", cursive; font-size: 58px; color: var(--ink);
  }
  .title {
    position: absolute; left: 0; width: 990px; top: 183px; text-align: center;
    font-family: "Montserrat", sans-serif; font-weight: 800; font-size: 40px;
    letter-spacing: 0.5px; color: var(--navy);
  }
  .awarded-label {
    position: absolute; left: 0; width: 990px; top: 248px; text-align: center;
    font-family: "Montserrat", sans-serif; font-weight: 700; font-size: 25px;
    letter-spacing: 12px; color: var(--navy);
  }
  .name-line {
    position: absolute; left: 145px; top: 362px; width: 705px;
    border-top: 2px dashed var(--rule);
  }
  .completion-note {
    position: absolute; left: 0; width: 990px; top: 408px; text-align: center;
    font-family: "Tinos", serif; font-size: 19px; color: #1c2430;
  }
  .date-line {
    position: absolute; left: 402px; top: 528px; width: 180px;
    border-top: 2px solid var(--rule);
  }
  .date-label {
    position: absolute; left: 380px; width: 230px; top: 524px; text-align: center;
    font-family: "Great Vibes", cursive; font-size: 34px; color: var(--ink);
  }
</style>
</head>
<body>
<main class="certificate">
  <svg class="waves" viewBox="0 0 1200 848" aria-hidden="true">
    <path d="M720 0 C860 30 1000 70 1200 150 L1200 0 Z" fill="var(--mist)" opacity="0.7"/>
    <path d="M860 0 C960 40 1080 90 1200 175 L1200 0 Z" fill="var(--sky)" opacity="0.55"/>
    <path d="M980 0 C1060 20 1130 50 1200 95 L1200 0 Z" fill="var(--sea)" opacity="0.8"/>
    <path d="M1060 0 C1110 10 1160 25 1200 45 L1200 0 Z" fill="var(--sea-deep)"/>

    <path d="M0 440 C80 500 150 620 200 848 L0 848 Z" fill="var(--sky)" opacity="0.6"/>
    <path d="M0 470 C60 540 110 650 130 848 L0 848 Z" fill="var(--sea)" opacity="0.8"/>
    <path d="M0 580 C240 600 520 700 760 848 L0 848 Z" fill="var(--mist)" opacity="0.75"/>
    <path d="M0 620 C260 640 560 720 900 848 L0 848 Z" fill="var(--sky)" opacity="0.55"/>
    <path d="M0 690 C300 700 620 770 820 848 L0 848 Z" fill="var(--sea)" opacity="0.75"/>
    <path d="M0 760 C300 770 560 810 680 848 L0 848 Z" fill="var(--sea-deep)" opacity="0.85"/>
    <path d="M700 848 C900 790 1060 800 1200 810 L1200 848 Z" fill="var(--mist)" opacity="0.8"/>
  </svg>

  <div class="island-map" role="img" aria-label="Map of the island where the challenge is run"></div>
  <div class="runner-figure" role="img" aria-label="Silhouette of a runner in stride"></div>

  <p class="heading-script">Certificate</p>
  <h1 class="title">BRISORA 50K RUNNING CHALLENGE</h1>
  <p class="awarded-label">AVARDED TO</p>
  <div class="name-line"></div>
  <p class="completion-note">Successfully finished the Brisora 50K Running Challenge.</p>
  <div class="date-line"></div>
  <p class="date-label">Date Awarded</p>
</main>
</body>
</html>
```